Kestrel Signs Facebook Banner Design

Design a facebook banner for a sign company. I would like to have a modern approach to it.

Product Offering:
Signs
Banners
Decals
Commercial Wraps

```html
<!DOCTYPE html>
<html lang="en">
<head>
<meta charset="utf-8">
<title>Kestrel Signs – Facebook Cover</title>
<link rel="stylesheet" href="https://fonts.googleapis.com/css2?family=Roboto:wght@700;900&display=swap">
<style>
  :root {
    --brand-red: #e8333a;
    --brand-grey: #4f4f4f;
    --paper: #ffffff;
    --stage: #eef0f3;
    --check-light: #d6d6d6;
    --type: "Roboto", Arial, sans-serif;
  }
  * { margin: 0; padding: 0; box-sizing: border-box; }
  html, body { width: 1200px; height: 715px; overflow: hidden; background: var(--stage); }
  .cover {
    position: absolute; left: 0; top: 137px;
    width: 1200px; height: 441px;
    background: var(--paper); overflow: hidden;
    font-family: var(--type);
  }
  .cover__shapes { position: absolute; inset: 0; }
  .tagline {
    position: absolute; left: 0; width: 1200px; top: 42px;
    text-align: center; font-size: 27px; font-weight: 700; color: var(--brand-grey);
  }
  .brand-name {
    position: absolute; left: 0; width: 1200px; top: 80px;
    text-align: center; font-weight: 900; color: var(--brand-red);
    line-height: 1; text-transform: uppercase;
  }
  .brand-name__main { display: block; font-size: 70px; letter-spacing: 2px; }
  .brand-name__sub { display: block; font-size: 56px; margin-top: 6px; letter-spacing: 3px; }
  .services {
    position: absolute; top: 228px; height: 64px; left: 273px; width: 654px;
    display: flex; align-items: center;
    color: var(--paper); font-weight: 700; font-size: 40px;
  }
  .services__item { position: absolute; top: 0; line-height: 64px; text-align: center; }
  .services__item--design { left: 0; width: 240px; }
  .services__item--print { left: 218px; width: 216px; }
  .services__item--install { left: 436px; width: 218px; }
  .contact {
    position: absolute; top: 328px; height: 31px; left: 415px; width: 392px;
    color: var(--paper); font-weight: 700; font-size: 22px; line-height: 31px;
  }
  .contact__label { position: absolute; left: 28px; }
  .contact__phone { position: absolute; left: 193px; letter-spacing: 0.5px; }
  .website {
    position: absolute; left: 0; width: 1224px; top: 372px;
    text-align: center; font-size: 27px; font-weight: 700; color: var(--brand-grey);
  }
</style>
</head>
<body>
  <section class="cover">
    <svg class="cover__shapes" viewBox="0 0 1200 441" width="1200" height="441" aria-hidden="false">
      <defs>
        <linearGradient id="check-fade-left" x1="0" y1="0" x2="0" y2="1">
          <stop offset="0" stop-color="#d9c9ca"/>
          <stop offset="0.6" stop-color="#f0888c"/>
          <stop offset="1" stop-color="#e8333a"/>
        </linearGradient>
        <linearGradient id="check-fade-right" x1="0" y1="1" x2="0" y2="0">
          <stop offset="0" stop-color="#e0a0a3"/>
          <stop offset="0.6" stop-color="#f0888c"/>
          <stop offset="1" stop-color="#e8333a"/>
        </linearGradient>
        <linearGradient id="billboard-tone" x1="0" y1="0" x2="1" y2="1">
          <stop offset="0" stop-color="#fbe3e4"/>
          <stop offset="1" stop-color="#f5b9bb"/>
        </linearGradient>
      </defs>
      <!-- side bands -->
      <polygon class="band band--left" points="0,0 181,0 53,441 0,441" fill="var(--brand-red)"/>
      <polygon class="band band--right" points="1142,0 1200,0 1200,441 1014,441" fill="var(--brand-red)"/>
      <polygon role="img" aria-label="Chequered flag pattern" points="0,0 181,0 128,180 0,180" fill="url(#check-fade-left)"/>
      <polygon role="img" aria-label="Chequered flag pattern" points="1091,260 1200,260 1200,441 1014,441" fill="url(#check-fade-right)"/>
      <!-- billboard artwork area -->
      <rect role="img" aria-label="Outline illustration of two roadside billboards" x="140" y="231" width="166" height="210" fill="url(#billboard-tone)"/>
      <!-- services pill -->
      <path d="M305,228 H496 L478,292 H305 A32,32 0 0 1 305,228 Z" fill="var(--brand-red)"/>
      <polygon points="505,228 707,228 689,292 487,292" fill="var(--brand-grey)"/>
      <path d="M716,228 H895 A32,32 0 0 1 895,292 H698 Z" fill="var(--brand-red)"/>
      <!-- contact bar -->
      <path d="M430,328 H800 Q797,350 785,359 H430 A15.5,15.5 0 0 1 430,328 Z" fill="var(--brand-red)"/>
      <path d="M430,328 H545 Q580,336 602,359 H430 A15.5,15.5 0 0 1 430,328 Z" fill="var(--brand-grey)"/>
      <!-- phone glyph -->
    </svg>

    <p class="tagline">Transform Your Brand with</p>
    <h1 class="brand-name">
      <span class="brand-name__main">Kestrel</span>
      <span class="brand-name__sub">Signs</span>
    </h1>

    <div class="services">
      <span class="services__item services__item--design">Design</span>
      <span class="services__item services__item--print">Print</span>
      <span class="services__item services__item--install">Instal</span>
    </div>

    <div class="contact">
      <span class="contact__label">Contact us</span>
      <span class="contact__phone">+1 604-555-0148</span>
    </div>

    <p class="website">www.kestrelsigns.ca</p>
  </section>
</body>
</html>
```